Breezeline Climate Crew WA Truck

I want a truck desing that screams Professional, Friendly and serious about work. you can find some of our work on our website, facebook and instagram.
https://breezelinecrew.example.com.au/
https://www.instagram.com/bzcrewox/
https://www.facebook.com/profile.php?id=70318825094631

The design needs to include our refrigeration license: AU38452 and electrical License: EC94031
I want the colours to be consistent with my Logo.

Key Notes to be included in the design, I want to let people know we do the following;
- Commercial and Residential
- Repairs, Service and Installation
- Reverse cycle ducted Air Conditioning
- Wall Split Air Conditioning
- Ceiling Cassettes
- Evaporative Air Conditioning
- Cool Rooms
- Display Fridges
- Beer Chillers

```html
<!DOCTYPE html>
<html lang="en">
<head>
<meta charset="utf-8">
<title>Breezeline Climate Crew WA – Truck Side Wrap</title>
<link rel="stylesheet" href="https://fonts.googleapis.com/css2?family=Montserrat:wght@700;800&family=Roboto+Condensed:ital,wght@1,700&family=Open+Sans:wght@400&display=swap">
<style>
  :root {
    --page-bg: #e6eaef;
    --panel-white: #f7f8f9;
    --panel-edge: #b9bec4;
    --navy: #1c3a78;
    --band-blue: #1677b8;
    --orange: #e8651d;
    --amber: #f2a31f;
    --red: #d0202a;
    --text-navy: #1f3f87;
    --text-grey: #5b5f66;
    --white: #ffffff;
    --unit-light: #eef0f2;
    --unit-shade: #c9cdd2;
  }
  * { box-sizing: border-box; margin: 0; padding: 0; }
  html, body {
    width: 1200px; height: 710px; overflow: hidden;
    background: var(--page-bg);
  }
  .wrap-panel {
    position: absolute; left: 20px; top: 78px;
    width: 1160px; height: 555px;
    background: var(--panel-white);
    border: 4px solid var(--panel-edge);
    overflow: hidden;
  }
  .wrap-graphics { position: absolute; inset: 0; }

  .brand-mark {
    position: absolute; left: 60px; top: 70px; width: 580px;
    display: flex; flex-direction: column; align-items: center; gap: 22px;
  }
  .brand-dot {
    width: 130px; height: 130px; border-radius: 50%;
    background: var(--band-blue);
  }
  .brand-name {
    font-family: "Montserrat", sans-serif; font-weight: 800;
    font-size: 38px; line-height: 1.15; text-align: center;
    color: var(--orange); text-transform: uppercase; letter-spacing: 1px;
  }

  .services-unit {
    position: absolute; left: 735px; top: 20px; width: 306px; height: 95px;
    border-radius: 8px;
    background: linear-gradient(180deg, var(--unit-light) 0%, var(--unit-light) 60%, var(--unit-shade) 100%);
  }
  .services-title {
    position: absolute; left: 735px; top: 26px; width: 306px;
    text-align: center;
    font-family: "Roboto Condensed", sans-serif; font-style: italic; font-weight: 700;
    font-size: 34px; letter-spacing: 1px; color: var(--red);
  }

  .service-list {
    position: absolute; left: 704px; top: 142px;
    list-style: none;
    font-family: "Roboto Condensed", sans-serif; font-style: italic; font-weight: 700;
    font-size: 22.5px; line-height: 32px; color: var(--text-navy);
  }
  .service-list li::before {
    content: "*"; color: var(--red); font-size: 18px; margin-right: 6px;
  }

  .licence-line {
    position: absolute; left: 704px; top: 454px;
    font-family: "Open Sans", sans-serif; font-size: 13.5px; color: var(--text-grey);
    word-spacing: 1px;
  }

  .contact-band {
    position: absolute; left: 0; right: 0; top: 490px; height: 65px;
    display: flex; align-items: center; padding: 0 28px 0 40px;
    justify-content: space-between;
    font-family: "Montserrat", sans-serif; color: var(--white);
  }
  .web-address { font-weight: 700; font-size: 27px; letter-spacing: 0.3px; }
  .phone-line { display: flex; align-items: center; gap: 10px; font-weight: 800; font-size: 34px; }
  .phone-icon { width: 32px; height: 32px; }
</style>
</head>
<body>
  <main class="wrap-panel">
    <svg class="wrap-graphics" viewBox="0 0 1152 547" width="1152" height="547" aria-hidden="true">
      <defs>
        <linearGradient id="bandFill" x1="0" y1="0" x2="1" y2="0">
          <stop offset="0" stop-color="#1c3a78"/>
          <stop offset="0.55" stop-color="#1c3a78"/>
          <stop offset="1" stop-color="#1677b8"/>
        </linearGradient>
      </defs>
      <path d="M0,330 C150,390 300,450 470,476 L1152,478 L1152,547 L0,547 Z" fill="url(#bandFill)"/>
      <path d="M440,470 C600,482 800,480 1152,476" fill="none" stroke="#e8651d" stroke-width="4"/>
      <path d="M0,318 C140,370 260,420 380,452" fill="none" stroke="#e8651d" stroke-width="6"/>
    </svg>

    <div class="brand-mark">
      <span class="brand-dot"></span>
      <p class="brand-name">Breezeline Climate<br>Crew WA</p>
    </div>

    <div class="services-unit" role="img" aria-label="Wall split air conditioner unit"></div>
    <h2 class="services-title">SERVICES</h2>

    <ul class="service-list">
      <li>Commercial and Residential</li>
      <li>Repairs, Service and Installation</li>
      <li>Reverse cycle ducted Air Conditioning</li>
      <li>Wall Split Air Conditioning</li>
      <li>Ceiling Cassettes</li>
      <li>Evaporative Air Conditioning</li>
      <li>Cool Rooms</li>
      <li>Display Fridges</li>
      <li>Beer Chillers</li>
    </ul>

    <p class="licence-line">License: AU38452&nbsp; License: EC94031</p>

    <footer class="contact-band">
      <span class="web-address">www.breezelinecrew.example.com.au</span>
      <span class="phone-line">
        <svg class="phone-icon" viewBox="0 0 32 32" aria-hidden="true">
          <circle cx="16" cy="16" r="15" fill="#e8651d"/>
          <path d="M11 8.5c1-.6 1.8-.3 2.3.6l1.3 2.6c.4.8.2 1.5-.5 2l-1 .7c.7 1.8 2 3.2 3.8 4l.8-1c.5-.6 1.3-.8 2-.4l2.6 1.3c.9.5 1.1 1.3.6 2.3-1 1.8-2.7 2.4-4.6 1.7-4-1.5-7-4.6-8.4-8.6-.6-1.9-.2-3.5 1.1-5.2z" fill="#ffffff"/>
        </svg>
        0400 555 018
      </span>
    </footer>
  </main>
</body>
</html>
```